Mental Health Therapy Website

I need a design for a mental health therapy website. It is a private practice. The business name is Brindle Counseling, PLLC. My name is Martin Hale, LMHC, NCC, DCC. I would like some of the features/menus to be Home; Welcome/About Me, Rates and Services, Common Questions, and Contact.
If possible I would like a blog on the main page that I can update with articles I write. I would like the contact page to feature a map to my location (4318 Cedarbend Ave. E, Lakewood, WA 98499).
I would like to place a small photo of me on the Welcome/About page.
I am new to this so if I am forgetting anything, please ask me!!
I will upload my logo so you can fit it and the color scheme into the design.
Thank you so very much!

```html
<!DOCTYPE html>
<html lang="en">
<head>
<meta charset="utf-8">
<title>Brindle Counseling</title>
<link href="https://fonts.googleapis.com/css2?family=PT+Sans:wght@400;700&display=swap" rel="stylesheet">
<style>
:root{
  --blue:#3dbbe8;
  --link:#2f8fc7;
  --navy:#1d5aa6;
  --ink:#333;
  --band:#e6e6e6;
  --panel:#f1f1f1;
  --footer:#333333;
  --white:#fff;
}
*{margin:0;padding:0;box-sizing:border-box}
html,body{width:1200px;height:1135px;overflow:hidden;background:var(--white);font-family:"PT Sans",Arial,sans-serif;color:var(--ink)}
.page{position:relative;width:1200px;height:1135px}
.abs{position:absolute}
.brand{left:149px;top:28px;display:flex;align-items:center;gap:10px}
.brand-dot{width:64px;height:64px;border-radius:50%;background:var(--navy);flex:none}
.brand-name{font-size:26px;color:var(--navy);line-height:1;white-space:nowrap}
.nav{display:flex;align-items:center;font-size:12px;color:#555;white-space:nowrap}
.nav span.sep{margin:0 11px;color:#777}
.nav-top{right:128px;top:73px}
.band{left:0;top:120px;width:1200px;height:339px;background:var(--band)}
.slide-photo{left:149px;top:139px;width:567px;height:290px;background:radial-gradient(circle at 30% 40%,#5b8fd6 0,#c9dcf2 35%,#eef4fb 70%,#f8fbfe 100%)}
.slide-panel{left:716px;top:139px;width:359px;height:290px;background:var(--blue);color:var(--white);font-size:19px;line-height:24px;padding:74px 84px 0 36px}
.slide-shadow{left:716px;top:429px;width:260px;height:10px;background:radial-gradient(ellipse at 50% 0,rgba(0,0,0,.28),rgba(0,0,0,0) 70%)}
.slide-tag{left:375px;top:170px;width:134px;height:134px;background:var(--blue);color:var(--white);font-size:21px;text-align:right;padding:11px 12px 0 0}
.slide-frame{left:326px;top:287px;width:68px;height:68px;border:1px solid rgba(255,255,255,.9)}
.arrow{width:29px;height:27px;background:#777;display:flex;align-items:center;justify-content:center}
.welcome{left:149px;top:492px;font-size:20px;color:#222;letter-spacing:.2px;font-weight:400}
.photo{top:538px;width:293px;height:143px}
.photo-about{left:149px;background:linear-gradient(90deg,#4f5a3c 0,#8a7a62 45%,#6a6b4c 80%,#252122 80%)}
.photo-fruit{left:464px;background:linear-gradient(135deg,#f0a020 0,#d8303a 35%,#7a2030 55%,#9cc83c 80%,#6fa02a 100%)}
.social{left:782px;top:540px;width:293px;height:141px;background:var(--panel);padding:12px 0 0 32px}
.social h3,.col-title{font-weight:400;font-size:15px;color:#222}
.social h3 em,.col-title em{font-style:normal;color:var(--link)}
.social ul{list-style:none;margin-top:7px}
.social li{display:flex;align-items:center;gap:12px;font-size:12.5px;color:#777;height:31px}
.social .ico{width:24px;height:24px;border-radius:50%}
.ico.chirp{background:#4aa8dc}.ico.page{background:#2f4d8f}.ico.pin{background:#cc2127}
.col-title{top:698px}
.copy{font-size:9.8px;line-height:12.6px;color:#444;width:290px}
.bullets{left:464px;list-style:none;width:295px}
.bullets li{position:absolute;left:0;display:flex;gap:15px}
.bullets svg{flex:none;margin-top:2px}
.cats{left:782px;top:738px;list-style:none;font-size:11.5px;color:var(--link)}
.cats li{position:absolute;white-space:nowrap;left:0}
.footer{left:0;top:1052px;width:1200px;height:83px;background:var(--footer)}
.foot-brand{left:151px;top:1073px;gap:6px}
.foot-brand .brand-dot{width:38px;height:38px}
.foot-brand .brand-name{font-size:14px;line-height:15px}
.nav-foot{left:302px;top:1087px;color:#ddd}
.nav-foot span.sep{color:#bbb}
.rights{right:125px;top:1087px;font-size:12px;color:#ccc}
</style>
</head>
<body>
<div class="page">
  <header>
    <div class="abs brand"><div class="brand-dot"></div><div class="brand-name">Brindle<br>Counseling</div></div>
    <nav class="abs nav nav-top">Home<span class="sep">|</span>About Me<span class="sep">|</span>Rates and Services<span class="sep" style="margin:0 18px">|</span>Common Questions<span class="sep" style="margin:0 14px">|</span>Contact.</nav>
  </header>

  <section>
    <div class="abs band"></div>
    <div class="abs slide-photo" role="img" aria-label="Close-up of blue glass marbles on a light surface"></div>
    <div class="abs slide-tag">HEALTH</div>
    <div class="abs slide-frame"></div>
    <div class="abs slide-panel">Lorem ipsum dolor sit amet, consectetur adipisicing elit, sed do eiusmod tempor incidi-dunt ut labore et dolore magna aliqua.</div>
    <div class="abs slide-shadow"></div>
    <div class="abs arrow" style="left:163px;top:276px"><svg width="12" height="14" viewBox="0 0 12 14"><path d="M10 1 2 7l8 6" fill="none" stroke="#fff" stroke-width="2"/></svg></div>
    <div class="abs arrow" style="left:1032px;top:276px"><svg width="12" height="14" viewBox="0 0 12 14"><path d="M2 1l8 6-8 6" fill="none" stroke="#fff" stroke-width="2"/></svg></div>
  </section>

  <main>
    <h1 class="abs welcome">WELCOME TO OUR WEBSITE</h1>

    <div class="abs photo photo-about" role="img" aria-label="Portrait photo of the therapist"></div>
    <h2 class="abs col-title" style="left:150px">About <em>Dr Martin Hale</em></h2>
    <p class="abs copy" style="left:149px;top:740px">Lorem ipsum dolor sit amet, consectetur adipisicing elit, sed do eiusmod tempor incididunt ut labore et dolore magna aliqua. Ut enim ad minim veniam, quis nostrud exercitation ullamco laboris nisi ut aliquip ex ea commodo consequat.</p>

    <div class="abs photo photo-fruit" role="img" aria-label="Bowl of fresh fruit with strawberries, grapes and citrus"></div>
    <h2 class="abs col-title" style="left:465px">Resource By <em>Dr Martin Hale</em></h2>
    <p class="abs copy" style="left:465px;top:740px">Lorem ipsum dolor sit amet, consectetur adipisicing elit, sed do eiusmod tempor incididunt ut labore et dolore magna aliqua. Ut enim ad minim veniam, quis nostrud exercitation ullamco laboris nisi ut aliquip ex ea commodo consequat.</p>
    <ul class="abs bullets" style="top:0">
      <li style="top:805px"><svg width="9" height="8" viewBox="0 0 9 8"><path d="M1 1l3 3-3 3M5 1l3 3-3 3" fill="none" stroke="#2f8fc7" stroke-width="1.4"/></svg><span class="copy" style="width:265px">Lorem ipsum dolor sit amet, consectetur adipisicing elit, sed do eiusmod tempor incididunt ut labore et dolore magna aliqua. Ut enim ad minim veniam,</span></li>
      <li style="top:861px"><svg width="9" height="8" viewBox="0 0 9 8"><path d="M1 1l3 3-3 3M5 1l3 3-3 3" fill="none" stroke="#2f8fc7" stroke-width="1.4"/></svg><span class="copy" style="width:265px">Lorem ipsum dolor sit amet, consectetur adipisicing elit, sed do eiusmod tempor incididunt ut labore et dolore magna aliqua. Ut enim ad minim veniam,</span></li>
      <li style="top:926px"><svg width="9" height="8" viewBox="0 0 9 8"><path d="M1 1l3 3-3 3M5 1l3 3-3 3" fill="none" stroke="#2f8fc7" stroke-width="1.4"/></svg><span class="copy" style="width:265px">Lorem ipsum dolor sit amet, consectetur adipisicing elit, sed do eiusmod tempor incididunt ut labore et dolore magna aliqua. Ut enim ad minim veniam,</span></li>
    </ul>

    <aside class="abs social">
      <h3>Social <em>Links</em></h3>
      <ul>
        <li><span class="ico chirp"></span>Get in Chirp</li>
        <li><span class="ico page"></span>Follow on Facepage</li>
        <li><span class="ico pin"></span>Find Pinboard</li>
      </ul>
    </aside>
    <h2 class="abs col-title" style="left:782px">Category</h2>
    <ul class="abs cats">
      <li style="top:0">Meet Your mental health therapst</li>
      <li style="top:24px">Common Questions</li>
      <li style="top:47px">New Patient Form &amp; Patient Resources</li>
      <li style="top:73px">Request an Appointment</li>
    </ul>
  </main>

  <footer>
    <div class="abs footer"></div>
    <div class="abs brand foot-brand"><div class="brand-dot"></div><div class="brand-name">Brindle<br>Counseling</div></div>
    <nav class="abs nav nav-foot">Home<span class="sep">|</span>About Me<span class="sep">|</span>Rates and Services<span class="sep" style="margin:0 18px">|</span>Common Questions<span class="sep" style="margin:0 14px">|</span>Contact.</nav>
    <div class="abs rights">All Right Reserved 2014.</div>
  </footer>
</div>
</body>
</html>
```